Attention grabbing 6x9 postcard

We are looking to have an attention grabbing post card that be sent out to homeowners from our roofing company Olum Roofing. the concept is that on the front it will say something like (STOP THE KNOCKING!
Tired of roofers knocking on your door? Contact us because we value your time as much as you value the roof over your head."
Olum Roofing
OlumRoofing.com
877.612.OLUM
info@olumroofing.com

Please feel free to come up with something very creative. Once we pick the final design we will provide the copy.

```html
<!DOCTYPE html>
<html lang="en">
<head>
<meta charset="utf-8">
<title>Olum Roofing Postcard</title>
<link href="https://fonts.googleapis.com/css2?family=Poppins:wght@400;600;700;800&display=swap" rel="stylesheet">
<style>
:root{
  --backdrop:#52575b;
  --gold:#e9b23a;
  --ink:#0c0c0c;
  --charcoal:#2a2a2a;
  --white:#ffffff;
  --stamp:#e0e1e3;
  --slate:#6f7884;
}
*{margin:0;padding:0;box-sizing:border-box}
html,body{width:1200px;height:1200px;overflow:hidden}
body{background:var(--backdrop);font-family:"Poppins",sans-serif;position:relative}
.card{position:absolute;left:244px;width:720px;height:486px;background:var(--white);overflow:hidden}
.card--front{top:92px}
.card--back{top:631px}
.card svg.shapes{position:absolute;left:0;top:0;width:720px;height:486px}
.wordmark{position:absolute;font-family:"Poppins",sans-serif;font-weight:600;color:var(--gold);letter-spacing:.18em;white-space:nowrap}
.front-wordmark{left:0;width:324px;text-align:center;top:136px;font-size:22px}
.headline{position:absolute;left:50px;top:201px;font-weight:800;font-size:53px;line-height:50px;letter-spacing:-.5px;white-space:nowrap}
.headline .line-gold{color:var(--gold);display:block}
.headline .line-white{color:var(--white);display:block}
.tagline{position:absolute;left:53px;top:330px;font-weight:700;font-size:16.2px;color:var(--ink);white-space:nowrap}
.body-copy{position:absolute;left:55px;top:375px;font-size:14.6px;line-height:18.5px;color:var(--ink);white-space:nowrap}
.phone{position:absolute;display:flex;align-items:center;font-weight:700;color:var(--ink);white-space:nowrap}
.phone svg{flex:none}
.front-phone{left:38px;top:438px;font-size:29px;gap:14px}
.contact{position:absolute;display:flex;align-items:center;gap:5px;font-size:11.5px;color:var(--white);white-space:nowrap}
.contact svg{flex:none}
.services-title{position:absolute;left:49px;top:14px;font-weight:800;font-size:26px;color:var(--ink)}
.service-label{position:absolute;width:160px;text-align:center;font-weight:700;font-size:12.6px;line-height:16px;color:var(--white)}
.back-phone{left:40px;top:390px;font-size:39px;gap:12px}
.back-wordmark{left:430px;width:155px;text-align:center;top:100px;font-size:13px}
.stamp{position:absolute;left:604px;top:49px;width:75px;height:74px;background:var(--stamp)}
</style>
</head>
<body>

<section class="card card--front">
  <svg class="shapes" viewBox="0 0 720 486">
    <defs>
      <linearGradient id="panelDark" x1="0" y1="0" x2="1" y2="1">
        <stop offset="0" stop-color="#0a0a0a"/><stop offset="1" stop-color="#333"/>
      </linearGradient>
      <linearGradient id="shingleTone" x1="0" y1="0" x2="1" y2="1">
        <stop offset="0" stop-color="#8c96a3"/><stop offset="1" stop-color="#4e565f"/>
      </linearGradient>
      <linearGradient id="workerTone" x1="0" y1="0" x2="1" y2="1">
        <stop offset="0" stop-color="#a9adb3"/><stop offset=".55" stop-color="#6b6f75"/><stop offset="1" stop-color="#4a4750"/>
      </linearGradient>
    </defs>
    <g stroke="var(--ink)" stroke-width="2" fill="none">
      <line x1="330" y1="0" x2="470" y2="70"/><line x1="345" y1="0" x2="480" y2="66"/>
      <line x1="365" y1="0" x2="490" y2="62"/><line x1="380" y1="0" x2="500" y2="58"/>
      <line x1="480" y1="0" x2="720" y2="120"/><line x1="500" y1="0" x2="720" y2="110"/>
      <line x1="520" y1="0" x2="720" y2="100"/><line x1="540" y1="0" x2="720" y2="90"/>
      <line x1="392" y1="330" x2="540" y2="418"/><line x1="400" y1="340" x2="520" y2="420"/>
      <line x1="410" y1="350" x2="500" y2="420"/>
    </g>
    <g stroke="var(--gold)" stroke-width="1.6">
      <line x1="570" y1="420" x2="720" y2="340"/><line x1="590" y1="420" x2="720" y2="350"/>
      <line x1="610" y1="420" x2="720" y2="362"/><line x1="630" y1="420" x2="720" y2="374"/>
    </g>
    <polygon points="0,140 20,140 42,160 42,360 20,380 0,380" fill="var(--ink)"/>
    <g fill="var(--white)">
      <polygon points="0,148 14,150 26,168 14,186 0,188"/>
      <polygon points="0,232 14,228 26,248 14,268 0,266"/>
      <polygon points="0,268 12,272 12,312 0,316"/>
      <polygon points="0,312 14,312 26,332 14,352 0,352"/>
    </g>
    <polygon points="32,180 345,180 395,210 395,322 32,322" fill="url(#panelDark)"/>
    <polygon points="30,322 380,322 406,340 384,362 20,362 30,346" fill="var(--gold)"/>
    <polygon points="550,27 716,123 716,315 550,411 384,315 384,123" fill="none" stroke="var(--ink)" stroke-width="10"/>
    <polygon points="550,36 708,128 708,310 550,402 392,310 392,128" fill="url(#workerTone)" role="img" aria-label="Photo of a roofer nailing asphalt shingles"/>
    <polygon points="388,27 472,75.5 472,172.5 388,221 304,172.5 304,75.5" fill="none" stroke="var(--ink)" stroke-width="8"/>
    <polygon points="388,34 466,79 466,169 388,214 310,169 310,79" fill="url(#shingleTone)" role="img" aria-label="Close-up photo of grey roof shingles"/>
    <polygon points="345,430 720,418 720,486 395,486 330,458" fill="url(#panelDark)"/>
    <polygon points="0,428 292,428 332,457 292,486 0,486" fill="var(--gold)"/>
  </svg>

  <div class="wordmark front-wordmark">OLUM ROOFING</div>
  <h1 class="headline"><span class="line-gold">STOP THE</span><span class="line-white">KNOCKING!</span></h1>
  <p class="tagline">Tired of roofers knocking on your door?</p>
  <p class="body-copy">Contact us because we value your time as<br>much as you value the roof over your head.</p>

  <div class="phone front-phone">
    <svg width="30" height="30" viewBox="0 0 30 30"><circle cx="15" cy="15" r="15" fill="var(--ink)"/><path d="M10 8c1-1 2-1 3 0l2 3c.5 1 0 2-1 2.5 .8 2 2 3.3 3.8 4 .6-1 1.6-1.4 2.5-.9l3 2c1 .7 1 2 0 3-2 2-5 1.5-9-2.5S8 10 10 8z" fill="var(--gold)"/></svg>
    <span>877.612.OLUM</span>
  </div>
  <div class="contact" style="left:386px;top:447px">
    <svg width="14" height="14" viewBox="0 0 14 14"><circle cx="7" cy="7" r="6" fill="none" stroke="var(--gold)" stroke-width="1.4"/><path d="M1 7h12M7 1c-3 3-3 9 0 12M7 1c3 3 3 9 0 12" stroke="var(--gold)" fill="none" stroke-width="1"/></svg>
    <span>OlumRoofing.com</span>
  </div>
  <div class="contact" style="left:532px;top:447px">
    <svg width="14" height="14" viewBox="0 0 14 14"><rect x="1" y="3" width="12" height="9" rx="1" fill="none" stroke="var(--gold)" stroke-width="1.5"/><path d="M1.5 4 7 8l5.5-4" stroke="var(--gold)" fill="none" stroke-width="1.4"/></svg>
    <span>info@olumroofing.com</span>
  </div>
</section>

<section class="card card--back">
  <svg class="shapes" viewBox="0 0 720 486">
    <defs>
      <linearGradient id="backDark" x1="0" y1="0" x2="1" y2="1">
        <stop offset="0" stop-color="#0a0a0a"/><stop offset=".5" stop-color="#2b2b2b"/><stop offset="1" stop-color="#0d0d0d"/>
      </linearGradient>
      <linearGradient id="houseTone" x1="0" y1="0" x2="0" y2="1"><stop offset="0" stop-color="#a9b7c6"/><stop offset="1" stop-color="#8a7a68"/></linearGradient>
      <linearGradient id="stormTone" x1="0" y1="0" x2="0" y2="1"><stop offset="0" stop-color="#b8c0c8"/><stop offset="1" stop-color="#4c5560"/></linearGradient>
      <linearGradient id="buildTone" x1="0" y1="0" x2="0" y2="1"><stop offset="0" stop-color="#8fb0d4"/><stop offset=".5" stop-color="#7a5a3e"/><stop offset="1" stop-color="#5a4630"/></linearGradient>
      <linearGradient id="tarpTone" x1="0" y1="0" x2="0" y2="1"><stop offset="0" stop-color="#5d8a4e"/><stop offset=".5" stop-color="#3f8fd8"/><stop offset="1" stop-color="#7d7a76"/></linearGradient>
    </defs>
    <polygon points="0,0 400,0 400,486 0,486" fill="url(#backDark)"/>
    <polygon points="0,0 245,0 400,90 400,100 355,100 295,53 42,53 0,30" fill="var(--gold)"/>
    <g stroke="var(--white)" stroke-width="2.2">
      <line x1="265" y1="0" x2="400" y2="80"/><line x1="285" y1="0" x2="400" y2="68"/>
      <line x1="305" y1="0" x2="400" y2="56"/><line x1="325" y1="0" x2="400" y2="44"/>
      <line x1="400" y1="425" x2="310" y2="486"/><line x1="400" y1="440" x2="330" y2="486"/>
      <line x1="400" y1="455" x2="350" y2="486"/>
    </g>
    <line x1="201" y1="74" x2="201" y2="370" stroke="#777" stroke-width="1"/>
    <line x1="51" y1="217" x2="348" y2="217" stroke="#777" stroke-width="1"/>
    <g stroke="var(--gold)" stroke-width="1.6">
      <polygon points="117,66 161,91.5 161,142.5 117,168 73,142.5 73,91.5" fill="url(#houseTone)" role="img" aria-label="Photo of a house gable roof"/>
      <polygon points="284,66 328,91.5 328,142.5 284,168 240,142.5 240,91.5" fill="url(#stormTone)" role="img" aria-label="Photo of storm-damaged shingles"/>
      <polygon points="117,228 161,253.5 161,304.5 117,330 73,304.5 73,253.5" fill="url(#buildTone)" role="img" aria-label="Photo of a house under construction"/>
      <polygon points="284,228 328,253.5 328,304.5 284,330 240,304.5 240,253.5" fill="url(#tarpTone)" role="img" aria-label="Photo of a roof covered with a blue tarp"/>
    </g>
    <polygon points="0,386 400,386 400,430 385,441 0,441 0,400" fill="var(--gold)"/>
  </svg>

  <h2 class="services-title">OUR SERVICES</h2>
  <p class="service-label" style="left:37px;top:172px">Retail/commercial<br>Roof replacement</p>
  <p class="service-label" style="left:204px;top:172px">Storm Damage<br>Roof Replacement</p>
  <p class="service-label" style="left:37px;top:339px">New<br>Construction</p>
  <p class="service-label" style="left:204px;top:335px">Repairs &amp;<br>Restoration</p>

  <div class="phone back-phone">
    <svg width="34" height="34" viewBox="0 0 30 30"><circle cx="15" cy="15" r="15" fill="var(--ink)"/><path d="M10 8c1-1 2-1 3 0l2 3c.5 1 0 2-1 2.5 .8 2 2 3.3 3.8 4 .6-1 1.6-1.4 2.5-.9l3 2c1 .7 1 2 0 3-2 2-5 1.5-9-2.5S8 10 10 8z" fill="var(--gold)"/></svg>
    <span>877.612.OLUM</span>
  </div>
  <div class="contact" style="left:32px;top:450px">
    <svg width="14" height="14" viewBox="0 0 14 14"><circle cx="7" cy="7" r="6" fill="none" stroke="var(--gold)" stroke-width="1.4"/><path d="M1 7h12M7 1c-3 3-3 9 0 12M7 1c3 3 3 9 0 12" stroke="var(--gold)" fill="none" stroke-width="1"/></svg>
    <span>OlumRoofing.com</span>
  </div>
  <div class="contact" style="left:167px;top:450px">
    <svg width="14" height="14" viewBox="0 0 14 14"><rect x="1" y="3" width="12" height="9" rx="1" fill="none" stroke="var(--gold)" stroke-width="1.5"/><path d="M1.5 4 7 8l5.5-4" stroke="var(--gold)" fill="none" stroke-width="1.4"/></svg>
    <span>info@olumroofing.com</span>
  </div>

  <div class="wordmark back-wordmark">OLUM ROOFING</div>
  <div class="stamp" aria-label="Stamp area"></div>
</section>

</body>
</html>
```